Career Counselor in need of a business card design

Hello Creatives! I'm in need of a business card design for a new company based in Georgia, USA called Pathways By Lantern.

Some things that may be helpful in creating your concept(s) include:

My Logo (Included in the Files section): There are three versions, two versions are in the second file. The all gold stacked (vertical) version is my primary logo and then there are two horizontal versions (one is all gold and the other is gold and grey).

My mission: to empower tweens through young adults to realize and actualize their CAREER ASPIRATIONS.
My vision: for tweens through young adults to LIVE LIFE ON PURPOSE and become CONTRIBUTING MEMBERS OF SOCIETY.

Biblical scriptures that support my ‘Why’: Psalms 127: 3-4(NIV) Children are a heritage from the Lord, offspring a reward from him. Like ARROWS in the hands of a warrior are children…. And Proverbs 29:18(JKV) Where there is no VISION, the people perish.

*Words in ALL CAPS are to emphasize what's important to me and may possibly provide you some inspiration (IDK - Have fun with it)!

Target Market(s)

My ideal customers are parents, guardians, and young adults.

Contact Information for Business Card

My name, degrees and credential: Delphine Marlow, M.S., Ed.S., NCC
Title: College and Career Coach and Consultant

Number: 555.318.2907
Address: 2718 Willowmere Avenue., Suite 405, Harlow Bend, QX 31299
Email: info@pathwaysbylantern.example
Website: www.pathwaysbylantern.example

My population: TWEENS • TEENS • EMERGING ADULTS
Services offered: One-On-One Sessions • Small Groups • Workshops

Colors

Designer to choose colors to be used in the design.

Requirements
Nice to have
• Either my mission or vision but I will understand if it does not all fit.
• My mission: To empower tweens through young adults to realize and actualize their career aspirations.
• My vision: For tweens through young adults to live life on purpose and become contributing members of society.

```html
<!DOCTYPE html>
<html lang="en">
<head>
<meta charset="utf-8">
<title>Pathways By Lantern — Business Card</title>
<link rel="stylesheet" href="https://fonts.googleapis.com/css2?family=Open+Sans:wght@400;600;700&display=swap">
<style>
  :root {
    --backdrop: #333333;
    --card: #f7f7f7;
    --gold: #c49a2c;
    --gold-faint: #efe6cc;
    --ink: #1f1f1f;
    --rule: #b9b9b9;
  }
  * { box-sizing: border-box; margin: 0; padding: 0; }
  html, body {
    width: 1200px; height: 1021px; overflow: hidden;
    background: var(--backdrop);
    font-family: "Open Sans", Arial, sans-serif;
    color: var(--ink);
  }
  .card {
    position: absolute; left: 250px;
    width: 700px; height: 400px;
    background: var(--card);
    box-shadow: 0 6px 18px rgba(0,0,0,.35);
    overflow: hidden;
  }
  .card--front { top: 80px; }
  .card--back { top: 541px; }

  /* Front */
  .front-mark {
    position: absolute; left: 50%; top: 80px; transform: translateX(-50%);
    display: flex; flex-direction: column; align-items: center; gap: 12px;
  }
  .brand-dot {
    width: 96px; height: 96px; border-radius: 50%;
    background: var(--gold);
  }
  .brand-name {
    font-weight: 600; color: var(--gold);
    font-size: 42px; letter-spacing: .5px; white-space: nowrap;
  }
  .audience {
    position: absolute; left: 0; right: 0; top: 292px;
    text-align: center; font-size: 17px; letter-spacing: .4px;
    text-transform: uppercase;
  }
  .audience .sep { color: var(--gold); margin: 0 6px; }

  /* Back */
  .back-mark {
    position: absolute; left: 46px; top: 40px;
    display: flex; align-items: center; gap: 14px;
  }
  .back-mark .brand-dot { width: 60px; height: 60px; }
  .back-mark .brand-name { font-size: 30px; }
  .decor-circle {
    position: absolute; right: -70px; bottom: -110px;
    width: 360px; height: 360px; border-radius: 50%;
    background: var(--gold-faint);
  }
  .person {
    position: absolute; left: 46px; top: 150px; width: 360px;
  }
  .person-name { color: var(--gold); font-weight: 700; font-size: 21px; white-space: nowrap; }
  .person-name .creds { font-weight: 400; font-size: 16px; }
  .person-title { font-size: 16px; margin-top: 2px; }
  .person-rule { height: 1px; background: var(--rule); margin: 10px 0 10px; width: 608px; }
  .contact-list { list-style: none; font-size: 16px; line-height: 25px; }
  .contact-list li { display: flex; align-items: center; gap: 8px; white-space: nowrap; }
  .contact-list svg { width: 14px; height: 14px; flex: none; }
  .services {
    position: absolute; right: 46px; top: 42px;
    text-align: right; font-size: 16px; line-height: 23px;
  }
  .address {
    position: absolute; right: 46px; bottom: 34px;
    text-align: right; font-size: 17px; line-height: 24px;
  }
  .address-rule { height: 1px; background: var(--rule); width: 260px; margin: 0 0 8px auto; }
</style>
</head>
<body>

<section class="card card--front" aria-label="Card front">
  <div class="front-mark">
    <span class="brand-dot" aria-hidden="true"></span>
    <span class="brand-name">Pathways By Lantern</span>
  </div>
  <p class="audience">Tweens<span class="sep">•</span>Teens<span class="sep">•</span>Emerging Adults</p>
</section>

<section class="card card--back" aria-label="Card back">
  <div class="decor-circle" aria-hidden="true"></div>

  <div class="back-mark">
    <span class="brand-dot" aria-hidden="true"></span>
    <span class="brand-name">Pathways By Lantern</span>
  </div>

  <div class="services">
    <p>One-on-one Sessions</p>
    <p>Small Groups</p>
    <p>Workshops</p>
  </div>

  <div class="person">
    <p class="person-name">Delphine Marlow<span class="creds">, M.S., Ed.S., NCC</span></p>
    <p class="person-title">College &amp; Career Coach and Consultant</p>
    <div class="person-rule"></div>
    <ul class="contact-list">
      <li>
        <svg viewBox="0 0 16 16" aria-hidden="true"><path fill="var(--gold)" d="M3.6 1.2l2.3 2.4-1.3 2c.9 2 2.6 3.7 4.6 4.6l2-1.3 2.4 2.3-1.5 2.3C6.9 13.2 2.8 9.1 1.3 3z"/></svg>
        555.318.2907
      </li>
      <li>
        <svg viewBox="0 0 16 16" aria-hidden="true"><rect x="1.5" y="3.5" width="13" height="9" fill="none" stroke="var(--gold)" stroke-width="1.4"/><path d="M1.5 3.5 8 9l6.5-5.5" fill="none" stroke="var(--gold)" stroke-width="1.4"/></svg>
        info@pathwaysbylantern.example
      </li>
      <li>
        <svg viewBox="0 0 16 16" aria-hidden="true"><g fill="none" stroke="var(--gold)" stroke-width="1.2"><circle cx="8" cy="8" r="6.3"/><ellipse cx="8" cy="8" rx="2.8" ry="6.3"/><path d="M1.7 8h12.6M2.8 4.7h10.4M2.8 11.3h10.4"/></g></svg>
        www.pathwaysbylantern.example
      </li>
    </ul>
  </div>

  <div class="address">
    <div class="address-rule"></div>
    <p>2718 Willowmere Avenue</p>
    <p>Suite 405</p>
    <p>Harlow Bend, QX 31299</p>
  </div>
</section>

</body>
</html>
```